Brennick Holdings Business Cards

These are professional business cards that are for my family office.
Put fake emails and phone numbers as of now until I finalize those components. This family office controls my families investments, assets, and future. The cards should be professional.
..
.
.
.
I just uploaded another variation of a logo I would like to see as a business card to I am inbeteen which logo to use

Target Market(s)

business

Industry/Entity Type

business

Contact Information for Business Card

Professional, wealth related, finance related.

Requirements
Must have
• Logo

```html
<!DOCTYPE html>
<html lang="en">
<head>
<meta charset="utf-8">
<title>Brennick Holdings Business Cards</title>
<link rel="stylesheet" href="https://fonts.googleapis.com/css2?family=Cormorant+SC:wght@500;600&family=Exo:wght@500&family=Montserrat:wght@600&family=Arimo:wght@400&display=swap">
<style>
  :root {
    --stage: #ababab;
    --card: #1a1a1a;
    --gold: #d4892a;
    --white: #ffffff;
    --serif: "Cormorant SC", "Times New Roman", serif;
    --sans: "Arimo", Arial, sans-serif;
  }
  * { box-sizing: border-box; margin: 0; padding: 0; }
  html, body { width: 1200px; height: 1000px; overflow: hidden; }
  body { background: var(--stage); position: relative; font-family: var(--sans); }

  .card {
    position: absolute; left: 207px; width: 786px; height: 449px;
    background: var(--card); border-radius: 18px;
  }
  .card--front { top: 43px; }
  .card--back { top: 513px; }

  .front-name {
    position: absolute; left: 0; right: 0; top: 168px;
    text-align: center; font-family: var(--serif); font-weight: 600;
    font-size: 62px; letter-spacing: 1px; color: var(--white);
  }
  .tagline {
    position: absolute; left: 0; right: 0; top: 398px;
    display: flex; justify-content: center; align-items: center; gap: 12px;
    color: var(--white); font-size: 18px; letter-spacing: 4.4px;
  }
  .tagline__dot { width: 10px; height: 10px; border-radius: 50%; background: var(--gold); }

  .person { position: absolute; left: 38px; top: 123px; }
  .person__name {
    font-family: "Exo", sans-serif; font-weight: 500; font-size: 31px;
    letter-spacing: 1.5px; color: var(--gold); line-height: 1;
  }
  .person__role {
    margin-top: 14px; font-family: "Montserrat", sans-serif; font-weight: 600;
    font-size: 20px; color: var(--white);
  }

  .contacts { position: absolute; left: 39px; top: 216px; list-style: none; }
  .contacts li {
    display: flex; align-items: flex-start; gap: 12px;
    color: var(--white); font-size: 20px; line-height: 32px;
  }
  .contacts svg { width: 22px; height: 22px; margin-top: 5px; flex: none; }

  .back-name {
    position: absolute; right: 50px; top: 374px;
    font-family: var(--serif); font-weight: 600; font-size: 34px;
    color: var(--white); line-height: 1;
  }
  .back-name__mark {
    position: absolute; right: 50px; top: 369px;
    width: 7px; height: 7px; border-radius: 50%; background: var(--gold);
  }
</style>
</head>
<body>

<section class="card card--front">
  <h1 class="front-name">Brennick Holdings</h1>
  <p class="tagline">
    <span class="tagline__dot"></span>
    STRATEGIC FINANCE. SUSTAINABLE WEALTH.
    <span class="tagline__dot"></span>
  </p>
</section>

<section class="card card--back">
  <div class="person">
    <p class="person__name">DANIEL HARTWELL</p>
    <p class="person__role">MANAGING DIRECTOR</p>
  </div>

  <ul class="contacts">
    <li>
      <svg viewBox="0 0 22 22" aria-hidden="true"><rect width="22" height="22" rx="3" fill="#d4892a"/><path d="M7 5h3l1 4-2 1a8 8 0 0 0 3 3l1-2 4 1v3c0 1-1 2-2 2A11 11 0 0 1 5 7c0-1 1-2 2-2z" fill="#fff"/></svg>
      044-987 654 321
    </li>
    <li>
      <svg viewBox="0 0 22 22" aria-hidden="true"><rect width="22" height="22" rx="3" fill="#d4892a"/><path d="M4 11l14-6-5 13-2-5z" fill="#fff"/></svg>
      info@mailname.com
    </li>
    <li>
      <svg viewBox="0 0 22 22" aria-hidden="true"><rect width="22" height="22" rx="3" fill="#d4892a"/><circle cx="11" cy="11" r="6" fill="none" stroke="#fff" stroke-width="1.6"/><path d="M5 11h12M11 5c-3 3-3 9 0 12M11 5c3 3 3 9 0 12" fill="none" stroke="#fff" stroke-width="1.3"/></svg>
      www.sitename.com
    </li>
    <li>
      <svg viewBox="0 0 22 22" aria-hidden="true"><rect width="22" height="22" rx="3" fill="#d4892a"/><path d="M11 18s-5-5-5-9a5 5 0 0 1 10 0c0 4-5 9-5 9z" fill="#fff"/><circle cx="11" cy="9" r="2" fill="#d4892a"/></svg>
      <span>4410 Harbor Crest Pkwy,<br>212-B, FL 32541</span>
    </li>
  </ul>

  <span class="back-name__mark"></span>
  <p class="back-name">Brennick Holdings</p>
</section>

</body>
</html>
```